DIN A5 flyer front already exists for the sales outlet

Hi. I'd like to create a DIN A5 flyer. The front should be your design. On the back, I'd like to include more information about our business.
The back should contain (images still need to be added):
Our services
Stamps – Buying and Selling
Whether you're looking for the Lorren Swallow, classic rarities, or the latest stamp issues – we offer almost everything you need for your collection. We're happy to order any stamps we don't currently have in stock. Do you want to sell a stamp collection or have you inherited one? We offer personalized consultations and will make you a fair offer.
Coins – Buying and Selling
From historical cantonal coins and Swiss federal coins dating back to 1850, to coveted gold coins – collectors and investors will find what they're looking for with us. Whether it's a 100-franc Seraphine, rare Batzen, or the Tessin gold Seraphine – we trade with passion and expertise. We are also happy to purchase your coin collection or individual valuable pieces.
Purchase of scrap gold and precious metals
We buy scrap gold, jewelry, watches, rings, gold coins, silver coins, silver billets, silver bars, and other precious metals at fair and transparent prices. Thanks to our many years of experience, you will receive a professional appraisal and market-based purchase prices – discreetly and without obligation.
Postage service for businesses
Save on postage costs: Businesses can purchase valid postage stamps from us at a discounted rate. A simple and attractive way to permanently reduce the shipping costs of your business mail.
Visit us at our new location:
Lindenhofweg 38, 4057 Basel
Feldhaus-Brenner AG – Your specialist shop for stamps, coins and precious metals.
People who want to sell their scrap gold, stamps or coins

```html
<!DOCTYPE html>
<html lang="en">
<head>
<meta charset="utf-8">
<title>Feldhaus-Brenner AG – Our Services</title>
<link rel="stylesheet" href="https://fonts.googleapis.com/css2?family=Cinzel:wght@500;600&family=Open+Sans:wght@400;600;700&family=Playfair+Display:ital,wght@0,500;1,400&display=swap">
<style>
  :root{
    --navy:#1b1a4d;
    --gold:#d8ad55;
    --gold-line:#d9b870;
    --red:#d41f2b;
    --ink:#1f1f1f;
    --panel:#eeeeee;
    --backdrop:#e9eaec;
    --white:#ffffff;
  }
  *{box-sizing:border-box;margin:0;padding:0}
  html,body{width:1200px;height:1137px;overflow:hidden;background:var(--backdrop)}
  .flyer{
    position:absolute;left:249.5px;top:52px;width:627px;height:890px;
    transform:scale(1.1605);transform-origin:0 0;
    background:var(--white);overflow:hidden;
    font-family:"Open Sans",Arial,sans-serif;color:var(--ink);
  }
  .header{position:absolute;left:0;top:0;width:627px;height:160px}
  .header svg{position:absolute;left:0;top:0}
  .brand{position:absolute;top:24px;left:0;width:100%;display:flex;justify-content:center;align-items:center;gap:7px}
  .brand-dot{width:12px;height:12px;border-radius:50%;background:var(--red)}
  .brand-name{font-family:"Open Sans",Arial,sans-serif;font-weight:700;font-size:17px;color:var(--red);letter-spacing:.5px;text-transform:uppercase}
  .page-title{position:absolute;top:70px;width:100%;text-align:center;font-family:"Cinzel",serif;font-weight:500;font-size:38px;color:var(--gold);letter-spacing:1px}

  .card{position:absolute;width:282px;height:303px;border:1.3px solid var(--gold-line);border-radius:6px;background:var(--white);overflow:hidden}
  .card-stamps{left:26px;top:163px}
  .card-coins{left:319px;top:163px}
  .card-gold{left:26px;top:475px}
  .card-postage{left:319px;top:475px}
  .side-art{position:absolute;left:0;top:0;width:117px;height:100%;background:linear-gradient(180deg,#ececec,#e4e4e4)}
  .side-art .art{position:absolute;left:14px;width:88px;border-radius:2px}
  .card-body{position:absolute;left:136px;right:12px;top:16px}
  .card-title{font-family:"Cinzel",serif;font-weight:500;color:var(--gold);font-size:25px;line-height:1}
  .card-sub{font-size:11.5px;font-weight:600;color:var(--navy);text-transform:uppercase;margin-top:3px;letter-spacing:.2px}
  .rule{display:block;width:45px;height:2px;background:var(--red);margin-top:8px}
  .card-text{font-size:10.3px;line-height:12.4px;margin-top:18px}
  .card-text p+p{margin-top:12px}
  .card-gold .card-body,.card-postage .card-body{left:13px;right:14px;top:20px}
  .card-gold .card-title{font-size:19px;line-height:21px;margin-top:2px}
  .card-gold .card-text,.card-postage .card-text{margin-top:10px}
  .card-postage .card-title{font-size:25px}
  .bottom-art{position:absolute;left:0;right:0;bottom:0;height:118px;background:linear-gradient(180deg,#f1f1f1,#e6e6e6)}
  .bottom-art .art{position:absolute}

  .skyline{position:absolute;left:26px;top:788px;width:184px;height:67px;background:linear-gradient(180deg,rgba(216,173,85,.15),rgba(216,173,85,.35))}
  .visit{position:absolute;left:220px;top:795px;width:210px;text-align:center}
  .ribbon{display:block;margin:0 auto;width:200px;height:18px;background:var(--red);color:var(--white);font-family:"Playfair Display",serif;font-size:10.5px;line-height:18px;letter-spacing:.6px;text-transform:uppercase;clip-path:polygon(0 0,100% 0,96% 50%,100% 100%,0 100%,4% 50%)}
  .address{font-family:"Playfair Display",serif;font-weight:500;text-transform:uppercase;font-size:16.5px;line-height:19px;letter-spacing:1px;margin-top:5px}
  .address .street{color:var(--navy);display:block}
  .address .city{color:var(--red);display:flex;align-items:center;justify-content:center;gap:10px}
  .address .city::before,.address .city::after{content:"";width:40px;height:1px;background:var(--gold-line)}
  .map{position:absolute;left:447px;top:788px;width:154px;height:66px;border-radius:4px;background:linear-gradient(135deg,#eef0f3,#dfe3ea)}
  .footer{position:absolute;left:0;bottom:0;width:100%;height:28px;background:var(--navy);text-align:center;color:#f2ead8;font-family:"Playfair Display",serif;font-style:italic;font-size:13.5px;line-height:28px;letter-spacing:.8px}
</style>
</head>
<body>
<main class="flyer">
  <header class="header">
    <svg width="627" height="160" viewBox="0 0 627 160" aria-hidden="true">
      <path d="M0 0H627V88Q420 150 313 150Q200 150 0 92Z" fill="var(--navy)"/>
      <path d="M0 92Q200 150 313 150Q420 150 627 88V96Q420 158 313 158Q200 158 0 100Z" fill="var(--red)"/>
    </svg>
    <div class="brand"><span class="brand-dot"></span><span class="brand-name">Feldhaus-Brenner</span></div>
    <h1 class="page-title">OUR SERVICES</h1>
  </header>

  <section class="card card-stamps">
    <div class="side-art">
      <div class="art" role="img" aria-label="Classic Swiss stamp with a swallow emblem" style="top:12px;height:86px;background:linear-gradient(135deg,#cfd8c4,#b9464a)"></div>
      <div class="art" role="img" aria-label="Red airmail stamp" style="top:104px;height:86px;left:32px;width:74px;background:linear-gradient(135deg,#e8cfcf,#b65a5c)"></div>
      <div class="art" role="img" aria-label="Pink classic franco stamp" style="top:206px;height:86px;background:linear-gradient(135deg,#f09ac3,#d94d93)"></div>
    </div>
    <div class="card-body">
      <h2 class="card-title">STAMPS</h2>
      <div class="card-sub">Buying and Selling</div>
      <span class="rule"></span>
      <div class="card-text">
        <p>Whether you're looking for the Lorren Swallow, classic rarities, or the latest stamp issues – we offer almost everything you need for your collection.</p>
        <p>We're happy to order any stamps we don't currently have in stock. Do you want to sell a stamp collection or have you inherited one? We offer personalized consultations and will make you a fair offer.</p>
      </div>
    </div>
  </section>

  <section class="card card-coins">
    <div class="side-art">
      <div class="art" role="img" aria-label="Gold commemorative coins" style="top:14px;height:62px;border-radius:40px;background:radial-gradient(circle,#e8c66a,#b08a2e)"></div>
      <div class="art" role="img" aria-label="Large gold coin" style="top:82px;height:88px;border-radius:50%;background:radial-gradient(circle,#efd27a,#b38b2c)"></div>
      <div class="art" role="img" aria-label="Swiss silver and copper coins" style="top:180px;height:106px;border-radius:44px;background:radial-gradient(circle,#cfcfcf,#8f8a86)"></div>
    </div>
    <div class="card-body">
      <h2 class="card-title">COINS</h2>
      <div class="card-sub">Buying and Selling</div>
      <span class="rule"></span>
      <div class="card-text">
        <p>From historical cantonal coins and Swiss federal coins dating back to 1850, to coveted gold coins – collectors and investors will find what they're looking for with us.</p>
        <p>Whether it's a 100-franc Seraphine, rare Batzen, or the Tessin gold Seraphine – we trade with passion and expertise. We are also happy to purchase your coin collection or individual valuable pieces.</p>
      </div>
    </div>
  </section>

  <section class="card card-gold">
    <div class="card-body">
      <div class="card-sub" style="margin-top:0">Purchase of</div>
      <h2 class="card-title">SCRAP GOLD &amp;<br>PRECIOUS METALS</h2>
      <span class="rule" style="margin-top:1px"></span>
      <div class="card-text">
        <p>We buy scrap gold, jewelry, watches, rings, gold coins, silver coins, silver billets, silver bars, and other precious metals at fair and transparent prices.</p>
        <p>Thanks to our many years of experience, you will receive a professional appraisal &amp; market-based purchase prices – discreetly and without obligation.</p>
      </div>
    </div>
    <div class="bottom-art">
      <div class="art" role="img" aria-label="Pile of gold jewelry and rings" style="left:24px;top:18px;width:236px;height:80px;border-radius:40px;background:radial-gradient(ellipse,#c9973c,#e9e6e2 72%)"></div>
    </div>
  </section>

  <section class="card card-postage">
    <div class="card-body">
      <h2 class="card-title">POSTAGE SERVICES</h2>
      <div class="card-sub">Of Business</div>
      <div class="card-text">
        <p>Save on postage costs: Businesses can purchase valid postage stamps from us at a discounted rate.</p>
        <p>A simple and attractive way to permanently reduce the shipping costs of your business mail.</p>
      </div>
    </div>
    <div class="bottom-art">
      <div class="art" role="img" aria-label="Orange Helvetia postage stamp" style="left:16px;top:10px;width:80px;height:90px;background:linear-gradient(135deg,#e6a74a,#c27a25)"></div>
      <div class="art" role="img" aria-label="Green, red and blue definitive stamps" style="left:106px;top:12px;width:150px;height:88px;background:linear-gradient(90deg,#8fc79a,#e07d80,#7fa2cf)"></div>
    </div>
  </section>

  <div class="skyline" role="img" aria-label="Gold line drawing of the Basel skyline"></div>
  <div class="visit">
    <span class="ribbon">Visit us at our new location</span>
    <div class="address">
      <span class="street">Lindenhofweg 38</span>
      <span class="city">4057 Basel</span>
    </div>
  </div>
  <div class="map" role="img" aria-label="Street map with a pin at Lindenhofweg 38, 4057 Basel"></div>

  <footer class="footer">We Look Forward to Welcoming You</footer>
</main>
</body>
</html>
```